Brochure design for HVAC Company

A classic tri-fold brochure design for an air conditioning, refrigeration, and heating company. Would like the designs to be simple (uncluttered), professional, and pull in the logo colors. Attached is the logo and a business card designs. The company name is Bluestem Valley Air Conditioning, Refrigeration, and Heating.

Target Market(s)

Businesses normally food establishments for refrigeration and ice machines. Looking to sell them on maintenance plan: Gold, Silver, and Bronze. The material should help them to understand the services offered: Maintenance, Servicing and Troubleshooting, and Installations of ice machines, commercial refrigeration, and walk-in freezers and air conditioning (duct, ductless, and rooftop)

Industry/Entity Type

Hvac

Font styles to use
Sans Serif

Requirements
Must have
• Include standard information, such as company name, at least two types of contact information (phone, email and post office address), a logo and tagline. It should also include a headline on the front and two or three brief items outlining benefits your organization can provide.
• Tagline is approximately 14 words and 66 characters.
• Looking to inform customers of services offered: maintenance three plans gold, silver, and bronze, servicing and troubleshooting, and installation.
• Products Serviced, maintained, and installed: Commercial refrigeration, Ice Machines, Air Conditioning (both duct, ductless, and rooftop), walk in freezers.
• Call to action is $100 off on signed maintenance contract. $50 off on first service call.
• Use lorem ipsum text to complement the details of the above information. I will add it later before printing.
• Use logo color scheme and any other colors that complement it.
• Would like this to be a word template.
Nice to have
• Can you make this a Microsoft Word template? Sketch is good, or adobe cs4 format.
Should not have
• Photos should NOT be focused on the homeowner. Should BE focused on the commercial side of the business. Photos can be from any of these product areas: commercial refrigeration, ice machine, walk in freezer boxes, and light roof top ac and heating units.

```html
<!DOCTYPE html>
<html lang="en">
<head>
<meta charset="utf-8">
<title>Bluestem Valley – Tri-fold Brochure</title>
<link href="https://fonts.googleapis.com/css2?family=Bebas+Neue&family=Montserrat:wght@300;400;600;700&display=swap" rel="stylesheet">
<style>
  :root{
    --blue:#3f5fae;
    --blue-deep:#2f4c95;
    --orange:#ec6b2c;
    --orange-soft:#f08a4f;
    --ink:#4a4f5c;
    --muted:#8a8f9b;
    --paper:#ffffff;
    --stage:#e8ebf1;
  }
  *{box-sizing:border-box;margin:0;padding:0}
  html,body{width:1200px;height:2699px;overflow:hidden}
  body{background:var(--stage);font-family:"Montserrat",sans-serif;color:var(--ink);position:relative}
  .section{position:absolute;left:0;width:1200px;height:900px}
  .section-label{position:absolute;right:60px;top:8px;font-family:"Bebas Neue",sans-serif;font-size:44px;letter-spacing:1px;color:var(--blue-deep)}
  .spread{position:absolute;left:60px;top:55px;width:1080px;height:835px;display:flex;box-shadow:0 8px 30px rgba(40,50,80,.18);background:var(--paper)}
  .panel{position:relative;width:360px;height:835px;overflow:hidden;background:var(--paper)}
  .panel + .panel{border-left:1px solid #eceef3}
  .cover-single{position:absolute;left:420px;top:55px;box-shadow:0 8px 30px rgba(40,50,80,.18)}
  .abs{position:absolute}
  .photo{position:absolute}
  .shape{position:absolute;left:0;top:0}

  /* cover */
  .cover-photo{left:0;top:0;width:360px;height:480px;background:linear-gradient(160deg,#dfe3e6 0%,#c9d3d8 30%,#e6b9a4 55%,#b9c7cf 75%,#eef0f2 100%)}
  .brand{position:absolute;display:flex;align-items:center;gap:10px}
  .brand-dot{width:22px;height:22px;border-radius:50%;background:var(--orange);flex:none}
  .brand-name{font-weight:700;font-size:19px;line-height:1.05;color:#fff;letter-spacing:.5px}
  .brand-name.on-light{color:var(--blue)}
  .brand-sub{position:absolute;font-size:7.5px;letter-spacing:1.2px;color:#fff;font-weight:600}
  .headline{position:absolute;font-size:27px;line-height:1.12;color:var(--blue);font-weight:300}
  .headline strong{color:var(--orange);font-weight:700;display:block}
  .url-bar{position:absolute;left:0;bottom:0;width:360px;height:62px;background:var(--orange);color:#fff;font-size:22px;font-weight:300;display:flex;align-items:center;justify-content:center;letter-spacing:.5px}

  /* outside */
  .about-title{font-weight:700;font-size:22px;color:#fff;letter-spacing:1px}
  .body-text{font-size:9.5px;line-height:1.55;color:var(--muted)}
  .body-text.light{color:#fff}
  .offer{color:#fff;font-weight:300;font-size:14px;line-height:1.2}
  .offer b{font-size:34px;font-weight:700}
  .offer sup{font-size:11px;font-weight:600}
  .offer em{font-style:normal;font-weight:700;color:#fff}
  .contact-title{font-weight:700;font-size:14px;color:var(--blue);letter-spacing:1px}
  .contact-title span{color:var(--orange)}
  .contact-list{list-style:none}
  .contact-list li{display:flex;align-items:center;gap:12px;font-size:10px;color:var(--ink);margin-bottom:12px}
  .contact-list svg{flex:none}

  /* inside */
  .section-head{font-weight:700;font-size:19px;color:var(--blue);line-height:1.1;letter-spacing:.5px}
  .section-head span{display:block;color:var(--orange);font-weight:400}
  .service-box{position:absolute;background:var(--blue);color:#fff;font-size:19px;font-weight:700;line-height:1.05;padding:12px 20px 12px 36px}
  .service-box span{display:block;font-weight:300}
  .service{position:absolute;left:26px;display:flex;gap:14px;width:310px}
  .service-icon{width:44px;height:44px;border-radius:50%;border:2px solid var(--orange);display:flex;align-items:center;justify-content:center;flex:none}
  .service-title{font-size:10.5px;font-weight:700;color:var(--blue);margin-bottom:4px}
  .service-title small{display:block;font-size:9px;font-weight:400;color:var(--blue)}
  .bullets{list-style:none}
  .bullets li{position:relative;padding-left:20px;font-size:9.5px;line-height:1.45;color:var(--muted);margin-bottom:12px}
  .bullets li::before{content:"";position:absolute;left:0;top:3px;width:8px;height:8px;background:var(--blue)}
  .products-head{font-weight:700;font-size:19px;color:var(--blue);line-height:1.15}
  .products-head span{color:var(--orange);font-weight:400;display:block}
  .corner-headline{position:absolute;right:26px;text-align:right;font-size:17px;line-height:1.2;color:#fff;font-weight:300}
  .corner-headline strong{font-weight:700;display:block}
  .diamond{position:absolute;transform:rotate(45deg);border:4px solid #fff;box-shadow:0 2px 6px rgba(0,0,0,.15)}
</style>
</head>
<body>

<!-- ========== COVER ========== -->
<section class="section" style="top:0">
  <h2 class="section-label">Cover Page</h2>
  <div class="panel cover-single">
    <div class="photo cover-photo" role="img" aria-label="Photo of a commercial refrigerated display case stocked with food"></div>
    <svg class="shape" width="360" height="835" viewBox="0 0 360 835"><polygon points="0,500 360,440 360,555 0,555" fill="var(--blue)"/></svg>
    <div class="brand" style="left:70px;top:478px"><span class="brand-dot"></span><span class="brand-name">BLUESTEM<br>VALLEY</span></div>
    <div class="brand-sub" style="left:70px;top:530px">AIR CONDITIONING · REFRIGERATION · HEATING</div>
    <div class="headline" style="left:36px;top:585px">Contrary to<strong>POPULAR BELIEF,<br>LOREM IPSUM IS</strong>not simply random<br>text</div>
    <div class="url-bar">bluestemvalleyhvac.com</div>
  </div>
</section>

<!-- ========== OUTSIDE ========== -->
<section class="section" style="top:900px">
  <h2 class="section-label">Outside Fold</h2>
  <div class="spread">
    <!-- inside flap -->
    <div class="panel">
      <div class="photo" style="left:0;top:0;width:360px;height:520px;background:linear-gradient(170deg,#c7cbcd 0%,#a9afb2 40%,#8b8a7d 70%,#b7a48a 100%)" role="img" aria-label="Photo of a stainless steel commercial ice machine"></div>
      <svg class="shape" width="360" height="835" viewBox="0 0 360 835">
        <polygon points="0,560 360,480 360,835 0,835" fill="var(--blue)"/>
        <polygon points="0,620 360,560 360,835 0,835" fill="var(--orange)"/>
      </svg>
      <div class="offer abs" style="left:40px;top:665px"><b>$100</b><sup>OFF</sup><br>on signed <em>maintenance</em> contract</div>
      <div class="offer abs" style="left:40px;top:745px"><b>$50</b><sup>OFF</sup><br>on first <em>service call</em>.</div>
    </div>
    <!-- back panel -->
    <div class="panel">
      <svg class="shape" width="360" height="835" viewBox="0 0 360 835">
        <polygon points="0,0 360,0 360,390 0,470" fill="var(--orange)"/>
        <polygon points="0,560 360,470 360,520 0,610" fill="var(--blue)"/>
      </svg>
      <div class="abs" style="left:36px;top:70px;width:290px">
        <div class="about-title">ABOUT US</div>
        <p class="body-text light" style="margin-top:14px">It is a long established fact that a reader will be distracted by the readable content of a page when looking at its layout. The point of using lorem ipsum is that it has a more or less normal distribution of letters, as opposed to using content here, content here, making it look like readable English for every visitor.</p>
      </div>
      <div class="diamond" style="left:105px;top:340px;width:150px;height:150px;background:linear-gradient(135deg,#9fb4c9,#5f7e9f 50%,#d9dee3)" role="img" aria-label="Photo of rooftop solar panels and HVAC units"></div>
      <div class="brand" style="left:40px;top:630px"><span class="brand-dot"></span><span class="brand-name on-light">BLUESTEM<br>VALLEY</span></div>
      <div class="abs" style="left:40px;top:690px">
        <div class="contact-title">CONTACT <span>US</span></div>
        <ul class="contact-list" style="margin-top:12px">
          <li><svg width="12" height="14" viewBox="0 0 12 14"><path d="M6 0a5 5 0 0 1 5 5c0 4-5 9-5 9S1 9 1 5a5 5 0 0 1 5-5z" fill="var(--blue)"/><circle cx="6" cy="5" r="2" fill="#fff"/></svg>PO Box 418, Bluestem Valley</li>
          <li><svg width="12" height="12" viewBox="0 0 12 12"><path d="M2 0l3 3-1.5 1.5a7 7 0 0 0 4 4L9 7l3 3-2 2C5 12 0 7 0 2z" fill="var(--blue)"/></svg>(555) 014-2290</li>
          <li><svg width="14" height="10" viewBox="0 0 14 10"><rect width="14" height="10" fill="var(--blue)"/><path d="M0 0l7 5 7-5" stroke="#fff" fill="none"/></svg>info@bluestemvalleyhvac.com</li>
          <li><svg width="12" height="12" viewBox="0 0 12 12"><circle cx="6" cy="6" r="5.2" stroke="var(--blue)" stroke-width="1.5" fill="none"/><path d="M1 6h10M6 1c-3 3-3 7 0 10M6 1c3 3 3 7 0 10" stroke="var(--blue)" fill="none"/></svg>bluestemvalleyhvac.com</li>
        </ul>
      </div>
    </div>
    <!-- cover -->
    <div class="panel">
      <div class="photo cover-photo" role="img" aria-label="Photo of a commercial refrigerated display case stocked with food"></div>
      <svg class="shape" width="360" height="835" viewBox="0 0 360 835"><polygon points="0,500 360,440 360,555 0,555" fill="var(--blue)"/></svg>
      <div class="brand" style="left:70px;top:478px"><span class="brand-dot"></span><span class="brand-name">BLUESTEM<br>VALLEY</span></div>
      <div class="brand-sub" style="left:70px;top:530px">AIR CONDITIONING · REFRIGERATION · HEATING</div>
      <div class="headline" style="left:36px;top:585px">Contrary to<strong>POPULAR BELIEF,<br>LOREM IPSUM IS</strong>not simply random<br>text</div>
      <div class="url-bar">bluestemvalleyhvac.com</div>
    </div>
  </div>
</section>

<!-- ========== INSIDE ========== -->
<section class="section" style="top:1800px">
  <h2 class="section-label">Inside Fold</h2>
  <div class="spread">
    <div class="photo" style="left:0;top:0;width:720px;height:240px;background:linear-gradient(100deg,#3a4a5c 0%,#7d98b0 25%,#c55d45 45%,#8aa2b8 65%,#33414f 100%);z-index:0" role="img" aria-label="Photo of a row of glass-door commercial freezers in a store"></div>
    <!-- services -->
    <div class="panel" style="background:transparent">
      <svg class="shape" width="360" height="835" viewBox="0 0 360 835">
        <rect x="0" y="240" width="360" height="595" fill="#fff"/>
        <polygon points="0,240 360,240 360,300 0,300" fill="var(--blue)"/>
        <polygon points="0,240 70,240 35,300" fill="var(--orange)"/>
        <polygon points="95,240 165,240 130,300" fill="#fff"/>
      </svg>
      <div class="service-box" style="left:130px;top:255px">SERVICES<span>OFFERED</span></div>
      <p class="body-text abs" style="left:26px;top:355px;width:300px">Contrary to popular belief, lorem ipsum is not simply random text. It has roots in a piece of classical Latin literature, making it over two thousand years old.</p>
      <div class="service" style="top:430px">
        <div class="service-icon"><svg width="22" height="22" viewBox="0 0 22 22"><path d="M4 4l14 14M18 4L4 18" stroke="var(--orange)" stroke-width="3" stroke-linecap="round"/></svg></div>
        <div><div class="service-title">MAINTENANCE 3 PLANS<small>GOLD, SILVER AND BRONZE</small></div><p class="body-text">Contrary to popular belief, lorem ipsum is not simply random text.</p></div>
      </div>
      <div class="service" style="top:530px">
        <div class="service-icon"><svg width="22" height="22" viewBox="0 0 22 22"><circle cx="11" cy="11" r="6" stroke="var(--orange)" stroke-width="3" fill="none"/><circle cx="11" cy="11" r="2" fill="var(--orange)"/></svg></div>
        <div><div class="service-title">SERVICING AND<br>TROUBLESHOOTING</div><p class="body-text">Contrary to popular belief, lorem ipsum is not simply random text.</p></div>
      </div>
      <div class="service" style="top:630px">
        <div class="service-icon"><svg width="22" height="22" viewBox="0 0 22 22"><path d="M11 2v11M6 8l5 5 5-5" stroke="var(--orange)" stroke-width="2.5" fill="none"/><path d="M3 14v5h16v-5" stroke="var(--orange)" stroke-width="2.5" fill="none"/></svg></div>
        <div><div class="service-title">INSTALLATION</div><p class="body-text">Contrary to popular belief, lorem ipsum is not simply random text. Contrary to popular belief, lorem.</p></div>
      </div>
    </div>
    <!-- why choose us -->
    <div class="panel" style="background:transparent">
      <svg class="shape" width="360" height="835" viewBox="0 0 360 835">
        <rect x="0" y="300" width="360" height="535" fill="#fff"/>
        <polygon points="0,240 360,240 360,300 0,300" fill="var(--blue)"/>
        <polygon points="200,0 360,0 360,240 250,240" fill="#fff"/>
      </svg>
      <div class="diamond" style="left:70px;top:230px;width:70px;height:70px;background:linear-gradient(135deg,#e9ecef,#b9c0c6)" role="img" aria-label="Photo of a walk-in freezer box"></div>
      <div class="diamond" style="left:225px;top:150px;width:110px;height:110px;background:linear-gradient(135deg,#f0b98a,#6b7f99 60%,#2f3c52)" role="img" aria-label="Photo of a restaurant terrace at dusk"></div>
      <div class="abs" style="left:26px;top:345px;width:305px">
        <div class="section-head">WHY<span>CHOOSE US</span></div>
        <p class="body-text" style="margin-top:14px">It is a long established fact that a reader will be distracted by the readable content of a page when looking at its layout. The point of using lorem ipsum is that it has a more or less normal distribution of letters, as opposed to using content here, making it look like readable English for every page.</p>
        <ul class="bullets" style="margin-top:18px">
          <li>Lorem ipsum dolor sit amet, consectetur adipiscing elit.</li>
          <li>Duis ac mi fringilla justo ultrices volutpat.</li>
          <li>Phasellus non libero eleifend, aliquet elit nec, sodales mauris.</li>
          <li>Sed viverra tortor varius vehicula tempor.</li>
        </ul>
      </div>
    </div>
    <!-- products -->
    <div class="panel">
      <svg class="shape" width="360" height="835" viewBox="0 0 360 835">
        <polygon points="0,0 360,0 360,230 0,230" fill="var(--orange)"/>
        <polygon points="0,230 360,230 360,300 0,300" fill="var(--blue)"/>
      </svg>
      <div class="corner-headline" style="top:30px">Contrary to<strong>POPULAR BELIEF,<br>LOREM IPSUM IS</strong>not simply random<br>text</div>
      <div class="diamond" style="left:20px;top:170px;width:90px;height:90px;background:linear-gradient(135deg,#f1c7a8,#8a6f8f 55%,#2e3550)" role="img" aria-label="Photo of a commercial dining room"></div>
      <div class="diamond" style="left:140px;top:190px;width:75px;height:75px;background:linear-gradient(135deg,#7a5aa0,#c97bb0 50%,#2c2746)" role="img" aria-label="Photo of a restaurant interior"></div>
      <div class="abs" style="left:26px;top:340px;width:305px">
        <div class="products-head"><span>PRODUCTS</span>SERVICED,<br>MAINTAINED, AND<br>INSTALLED:</div>
        <ul class="bullets" style="margin-top:22px">
          <li>Commercial refrigeration.</li>
          <li>Ice Machines.</li>
          <li>Air Conditioning<br>(both duct, ductless, and rooftop).</li>
          <li>Walk-in freezers.</li>
        </ul>
        <p class="body-text" style="margin-top:22px">It is a long established fact that a reader will be distracted by the readable content of a page when looking at its layout.</p>
      </div>
    </div>
  </div>
</section>

</body>
</html>
```